Virtual assistant company needs letterhead and email signature

We need a letterhead and email signature for our virtual assistant company - taskBeaver (small w capital F). Our tag line is plan ahead | taskBeaver

The colours we would like used are;

#81788c
#dddbe1

For reference our business cards have used #81788c background colour and #dddbe1 text

The fonts we would like used are

Lora
Proxima Nova

Please check out our twitter and facebook for style and feel

Twitter: @taskbeaver
www.examplebook.test/taskbeaver

Please also find attached our landing page and business cards for reference

Any questions please let us know

Thanks
E

Reason: We like the opportunity to receive furthur designs

```html
<!DOCTYPE html>
<html lang="en">
<head>
<meta charset="utf-8">
<title>taskBeaver — Letterhead &amp; Email Signature</title>
<link rel="stylesheet" href="https://fonts.googleapis.com/css2?family=Lora:wght@400&family=Open+Sans:wght@300;400;700&display=swap">
<style>
  :root {
    --brand: #7f768a;
    --brand-light: #dddbe1;
    --logo-ink: #ece9f0;
    --paper: #ffffff;
    --paper-shade: #f1f0f2;
    --rule: #d9d8dc;
    --name-ink: #7d7784;
    --stage: #ebeaed;
  }
  * { box-sizing: border-box; margin: 0; padding: 0; }
  html, body {
    width: 766px; height: 1200px; overflow: hidden;
    background: var(--stage);
  }
  body { position: relative; font-family: "Open Sans", Arial, sans-serif; }

  .letterhead {
    position: absolute; left: 16px; top: 18px; width: 730px; height: 945px;
    background: linear-gradient(135deg, var(--paper) 0%, var(--paper) 45%, var(--paper-shade) 100%);
    box-shadow: 0 1px 3px rgba(0,0,0,.25);
  }
  .letterhead__header {
    position: absolute; left: 0; top: 0; width: 100%; height: 107px;
    background: var(--brand);
    text-align: center; color: var(--logo-ink);
  }
  .brand-name {
    font-family: "Lora", Georgia, serif; font-weight: 400; color: var(--logo-ink);
    letter-spacing: .3px; line-height: 1;
  }
  .tagline { font-family: "Open Sans", Arial, sans-serif; font-weight: 300; color: var(--brand-light); }
  .letterhead__header .brand-name { font-size: 44px; padding-top: 24px; }
  .letterhead__header .tagline { font-size: 13.5px; margin-top: 6px; }

  .footer-rule {
    position: absolute; left: 0; width: 100%; height: 3px;
    border-top: 1px solid var(--rule); border-bottom: 1px solid var(--rule);
  }
  .letterhead .footer-rule { top: 887px; }

  .contact-band {
    position: absolute; left: 0; width: 100%;
    background: var(--brand); color: #fff; text-align: center;
    font-size: 11.5px; line-height: 15px;
  }
  .letterhead .contact-band { top: 892px; height: 53px; padding-top: 11px; }
  .contact-line { display: flex; justify-content: center; align-items: center; gap: 5px; }
  .contact-line svg { width: 10px; height: 10px; fill: none; stroke: #fff; stroke-width: 1.4; }
  .contact-line .web { letter-spacing: 1.3px; }
  .contact-line .gap { width: 2px; }

  .signature {
    position: absolute; left: 117px; top: 987px; width: 502px; height: 168px;
    background: var(--paper);
  }
  .signature__header {
    position: absolute; left: 0; top: 0; width: 100%; height: 38px;
    background: var(--brand); text-align: center;
  }
  .signature__header .brand-name { font-size: 21px; padding-top: 4px; }
  .signature__header .tagline { font-size: 6px; margin-top: 1px; }
  .signature__name {
    position: absolute; left: 0; top: 104px; width: 100%; text-align: center;
    font-weight: 700; font-size: 13px; line-height: 16px; color: var(--name-ink);
  }
  .signature .footer-rule { top: 124px; }
  .signature .contact-band { top: 129px; height: 39px; padding-top: 4px; font-size: 11px; line-height: 14px; }
</style>
</head>
<body>

<section class="letterhead">
  <header class="letterhead__header">
    <div class="brand-name">taskBeaver</div>
    <div class="tagline">plan ahead &nbsp;|&nbsp; taskBeaver</div>
  </header>
  <div class="footer-rule"></div>
  <footer class="contact-band">
    <div>12, Maple Court, Townsend, ST, 00000</div>
    <div class="contact-line">
      <svg viewBox="0 0 10 10"><path d="M2 1 L4 3 L3 4 Q4 6 6 7 L7 6 L9 8 L8 9 Q3 9 1 2 Z"/></svg>
      <span>555-010-0199</span>
      <svg viewBox="0 0 10 10"><rect x="1" y="2.5" width="8" height="5.5"/><path d="M1 2.5 L5 5.5 L9 2.5"/></svg>
      <span>info@taskBeaver.test</span><span class="gap"></span>
      <svg viewBox="0 0 10 10"><circle cx="5" cy="5" r="4"/><path d="M1 5 H9 M5 1 Q2.5 5 5 9 M5 1 Q7.5 5 5 9"/></svg>
      <span class="web">www.taskBeaver.test</span>
    </div>
  </footer>
</section>

<section class="signature">
  <header class="signature__header">
    <div class="brand-name">taskBeaver</div>
    <div class="tagline">plan ahead &nbsp;|&nbsp; taskBeaver</div>
  </header>
  <div class="signature__name">YOUR NAME</div>
  <div class="footer-rule"></div>
  <footer class="contact-band">
    <div>12, Maple Court, Townsend, ST, 00000</div>
    <div class="contact-line">
      <svg viewBox="0 0 10 10"><path d="M2 1 L4 3 L3 4 Q4 6 6 7 L7 6 L9 8 L8 9 Q3 9 1 2 Z"/></svg>
      <span>555-010-0199</span>
      <svg viewBox="0 0 10 10"><rect x="1" y="2.5" width="8" height="5.5"/><path d="M1 2.5 L5 5.5 L9 2.5"/></svg>
      <span>info@taskBeaver.test</span><span class="gap"></span>
      <svg viewBox="0 0 10 10"><circle cx="5" cy="5" r="4"/><path d="M1 5 H9 M5 1 Q2.5 5 5 9 M5 1 Q7.5 5 5 9"/></svg>
      <span class="web">www.taskBeaver.test</span>
    </div>
  </footer>
</section>

</body>
</html>
```